依頼詳細
★TOPラフ案について

・トップページの掲載内容はエクセルで作成した資料を添付しました。
仕様はワイヤーフレームのみですので、掲載情報が正しければ、お好きなデザインにて調整していただいて構いません。

掲載している情報のレイアウト通りではなくて大丈夫ですので
皆さまの感性にてお願いいたします。

・配置やデザイン等はアレンジしていただいて構いません。

・サイズは横幅2000pxで制作をお願いします。
縦に制限はありません。(コンテンツ幅は1100px~1200px内でお願いします。)
レスポンシブデザインのサイトで、bootstrap4を利用し、コーディングする予定になります。

・カラーイメージ
白を基調としてサブに青系、ワンポイントに赤色にてお願いします。

・ロゴ画像はヘッダーに入れる予定です。
(ロゴは青色(#00008B)で会社名ローマ字表示となります。頭文字は赤色(#FF3737)です。)

・デザインイメージ
誠実なデザインのイメージです。

デザイン選定後、決定した方には、正式な社名や連絡先を入れた修正をお願いしたいのと、
その他常識範囲で修正を依頼することもあります。
※以後、希望があれば中ページ作成及び他の案件コンテンツも継続してご依頼可能です。
ページ数
1ページ
希望イメージ
シンプル 複雑
単色 カラフル
暗い 明るい
日常 高級
遊び心 厳粛
未来的 伝統的
女性的 男性的
希望する色
青系
納品ファイル
• 高解像度JPG (.jpg)
• フォトショップ形式 (.psd)
補足説明
※ワイヤーフレーム通りのデザインでなくて、構いません。
メインビジュアル、素材などもお好みでデザインいただいて問題ございません。

仕様素材につきましてはZELNO定額素材内で使用可能な素材をご選択いただいてご使用ください。
(添付したデータ内にない素材でもご利用OKです。
その際は選定後素材№をお知らせください。)
■ 選んだ理由

依頼したイメージに沿ったデザインを作成いただけたためこちらのデザインに決めさせていただきました。

■ 提案者全員のお礼・コメント

多くの提案をいただき本当にありがとうございました。
次回の依頼の際も是非提案いただけますようお願いいたします。

```html
<!DOCTYPE html>
<html lang="ja">
<head>
<meta charset="UTF-8">
<title>梱包が変わると物流が変わる</title>
<link href="https://fonts.googleapis.com/css2?family=Noto+Sans+JP:wght@400;500;700;900&family=Montserrat:wght@600;700&display=swap" rel="stylesheet">
<style>
:root{
  --navy:#00008B;
  --blue:#1a2fa8;
  --sky:#7fa8e6;
  --red:#FF3737;
  --ink:#333a48;
  --mute:#8a8f99;
  --line:#dcdfe5;
  --gray:#eeeff2;
  --faint:#f1f2f5;
  --white:#ffffff;
}
*{margin:0;padding:0;box-sizing:border-box}
html,body{width:1200px;height:2728px;overflow:hidden;background:var(--white)}
body{font-family:"Noto Sans JP",sans-serif;color:var(--ink);position:relative}
.abs{position:absolute}

/* header */
.site-header{position:absolute;left:0;top:0;width:1200px;height:40px;background:var(--white);z-index:5}
.site-logo{left:24px;top:8px;font:700 20px "Montserrat",sans-serif;color:var(--navy);letter-spacing:1px}
.global-nav{left:330px;top:0;height:40px;display:flex;gap:0}
.global-nav a{display:block;padding:0 28px;line-height:40px;font-size:11px;color:var(--ink);text-decoration:none;border-left:1px solid var(--line)}
.global-nav a:last-child{border-right:1px solid var(--line)}
.header-tel{left:850px;top:9px;display:flex;align-items:center;gap:6px;font:700 17px "Montserrat",sans-serif;color:var(--navy)}
.header-contact{left:1030px;top:0;width:170px;height:40px;background:var(--navy);color:var(--white);font-size:11px;display:flex;align-items:center;justify-content:center;gap:6px}

/* hero */
.hero{left:0;top:40px;width:1200px;height:560px;overflow:hidden;background:linear-gradient(120deg,#4f78d6 0%,#8fb2ea 45%,#c9dbf4 100%)}
.hero-shape-a{left:-80px;top:0;width:520px;height:560px;background:#3c63c9;transform:skewX(-18deg);opacity:.55}
.hero-shape-b{left:300px;top:0;width:200px;height:560px;background:#a9c4ee;transform:skewX(-18deg);opacity:.45}
.hero-photo{left:440px;top:0;width:760px;height:560px;background:linear-gradient(100deg,rgba(220,230,245,0) 0%,#e6eef9 30%,#f3f6fb 100%)}
.hero-copy{left:112px;top:208px}
.hero-copy span{display:block;width:max-content;margin-bottom:24px;padding:6px 16px;background:var(--blue);color:var(--white);font-size:48px;font-weight:900;letter-spacing:3px;line-height:1.2;border-bottom:6px solid var(--red)}

/* section titles */
.bg-word{font:700 104px "Montserrat",sans-serif;color:var(--faint);letter-spacing:6px;line-height:1;white-space:nowrap}
.sec-title{display:flex;align-items:center;gap:16px;font-size:22px;font-weight:700;color:var(--ink)}
.sec-title::before{content:"";width:80px;height:3px;background:var(--red)}
.sec-text{font-size:11px;line-height:2.1;color:var(--ink)}
.btn-more{width:212px;height:40px;background:var(--navy);color:var(--white);font-size:12px;display:flex;align-items:center;justify-content:center;position:absolute}
.btn-more::after{content:"";position:absolute;right:16px;width:6px;height:6px;border-top:2px solid #fff;border-right:2px solid #fff;transform:rotate(45deg)}

/* about */
.about-band{left:0;top:1020px;width:1200px;height:66px;background:var(--gray)}
.about-photo{left:608px;top:660px;width:592px;height:500px;background:linear-gradient(160deg,#dfe3ea,#b9c0cb 60%,#8f98a4)}

/* business */
.business-band{left:600px;top:1510px;width:600px;height:74px;background:var(--gray)}
.business-photo{left:0;top:1168px;width:592px;height:392px;background:linear-gradient(150deg,#d8c2a0,#c7a478 55%,#b08c62)}

/* info */
.info-list{left:232px;top:1808px;width:700px}
.info-row{display:flex;align-items:center;height:50px;border-bottom:1px solid var(--line);font-size:11px}
.info-date{width:110px;color:var(--mute);font-family:"Montserrat",sans-serif;font-size:10px}
.info-tag{width:60px}
.info-tag i{display:inline-block;font-style:normal;background:var(--red);color:#fff;font-size:9px;padding:1px 8px}
.info-scroll{left:926px;top:1796px;width:6px;height:320px;background:var(--gray)}
.info-scroll::before{content:"";position:absolute;left:0;top:0;width:6px;height:90px;background:#9aa0aa}

/* contact */
.contact{left:0;top:2220px;width:1200px;height:240px;background:var(--navy)}
.contact .bg-word{color:rgba(255,255,255,.14);left:0;width:1200px;text-align:center;top:16px;font-size:92px}
.contact-title{left:0;width:1200px;top:74px;text-align:center;color:#fff;font-size:20px;font-weight:700}
.contact-box{top:128px;width:332px;height:86px;background:#fff;text-align:center;padding-top:10px}
.contact-box h3{font-size:10px;font-weight:500;color:var(--ink)}
.contact-tel{margin-top:4px;font:700 24px "Montserrat",sans-serif;color:var(--navy);display:flex;align-items:center;justify-content:center;gap:6px}
.contact-hours{font-size:9px;color:var(--mute);margin-top:2px}
.contact-mail{margin:10px auto 0;width:230px;height:34px;background:var(--navy);color:#fff;font-size:12px;display:flex;align-items:center;justify-content:center;gap:8px}

/* footer */
.footer-company{left:60px;top:2486px}
.footer-company h2{font-size:18px;font-weight:700;margin-bottom:10px}
.footer-company p{font-size:10px;line-height:1.9;color:var(--ink)}
.footer-company .tel{font:600 14px "Montserrat",sans-serif;color:var(--navy);margin-top:8px}
.footer-nav{left:600px;top:2550px;display:grid;grid-template-columns:repeat(4,130px);border-top:1px solid var(--line);border-bottom:1px solid var(--line)}
.footer-nav a{font-size:10px;color:var(--ink);text-decoration:none;line-height:34px;text-align:center}
.footer-sub{left:600px;top:2610px;display:grid;grid-template-columns:repeat(2,260px);border-bottom:1px solid var(--line)}
.footer-sub span{font-size:10px;line-height:34px;text-align:center;display:flex;align-items:center;justify-content:center;gap:6px}
.copyright{left:0;top:2692px;width:1200px;height:36px;background:var(--navy);color:#fff;font-size:9px;text-align:center;line-height:36px}
</style>
</head>
<body>

<header class="site-header">
  <div class="abs site-logo">LOGO</div>
  <nav class="abs global-nav">
    <a href="#">ホーム</a><a href="#">〇〇〇〇について</a><a href="#">業務案内</a><a href="#">お知らせ</a>
  </nav>
  <div class="abs header-tel">
    <svg width="16" height="16" viewBox="0 0 24 24"><path fill="#00008B" d="M6.6 10.8a15.1 15.1 0 006.6 6.6l2.2-2.2c.3-.3.7-.4 1-.2 1.1.4 2.3.6 3.6.6.6 0 1 .4 1 1V20c0 .6-.4 1-1 1A17 17 0 013 4c0-.6.4-1 1-1h3.5c.6 0 1 .4 1 1 0 1.3.2 2.5.6 3.6.1.3 0 .7-.2 1z"/></svg>
    000-000-0000
  </div>
  <div class="abs header-contact">
    <svg width="14" height="10" viewBox="0 0 14 10"><rect x=".5" y=".5" width="13" height="9" fill="none" stroke="#fff"/><path d="M.5.5l6.5 5 6.5-5" fill="none" stroke="#fff"/></svg>
    お問い合わせ
  </div>
</header>

<section class="abs hero">
  <div class="abs hero-shape-a"></div>
  <div class="abs hero-shape-b"></div>
  <div class="abs hero-photo" role="img" aria-label="作業着の男性が段ボール箱を抱えている写真"></div>
  <h1 class="abs hero-copy"><span>梱包が変わると</span><span>物流が変わる</span></h1>
</section>

<section class="about">
  <div class="abs about-band"></div>
  <div class="abs bg-word" style="left:24px;top:708px">ABOUT</div>
  <h2 class="abs sec-title" style="left:268px;top:768px">〇〇〇〇について</h2>
  <p class="abs sec-text" style="left:160px;top:860px;width:400px">当社は梱包と物流の現場をつなぐ会社です。<br>丁寧な作業で〇〇〇〇を<br>確かなサービスとしてお届けします。<br>お客様の声に寄り添い続けてまいります。</p>
  <a class="btn-more" style="left:268px;top:958px">詳しく見る</a>
  <div class="abs about-photo" role="img" aria-label="物流センターに並ぶトラックの写真"></div>
</section>

<section class="business">
  <div class="abs business-band"></div>
  <div class="abs business-photo" role="img" aria-label="倉庫で段ボール箱を梱包する作業員の写真"></div>
  <div class="abs bg-word" style="left:700px;top:1206px">PACKING</div>
  <h2 class="abs sec-title" style="left:680px;top:1268px">業務案内</h2>
  <p class="abs sec-text" style="left:760px;top:1340px;width:380px">梱包資材の設計から発送まで、一貫したサービスをご提供。<br>商品に合わせた最適な梱包で輸送品質を高め、<br>物流コストの削減にも貢献します。<br>お気軽にご相談ください。</p>
  <a class="btn-more" style="left:760px;top:1464px">詳しく見る</a>
</section>

<section class="info">
  <div class="abs bg-word" style="left:0;width:1200px;text-align:center;top:1680px">INFORMATION</div>
  <h2 class="abs sec-title" style="left:520px;top:1726px">お知らせ</h2>
  <div class="abs info-list">
    <div class="info-row"><span class="info-date">2022.01.01</span><span class="info-tag"><i>NEW</i></span><span>新しいお知らせのタイトルがここに入ります</span></div>
    <div class="info-row"><span class="info-date">2021.12.20</span><span class="info-tag"></span><span>年末年始の営業についてのお知らせです</span></div>
    <div class="info-row"><span class="info-date">2021.12.01</span><span class="info-tag"></span><span>ホームページをリニューアルいたしました</span></div>
    <div class="info-row"><span class="info-date">2021.11.15</span><span class="info-tag"></span><span>新しい梱包サービスの提供を開始しました</span></div>
    <div class="info-row"><span class="info-date">2021.11.01</span><span class="info-tag"></span><span>物流センターの稼働時間を変更いたします</span></div>
    <div class="info-row"><span class="info-date">2021.10.20</span><span class="info-tag"></span><span>採用情報を更新いたしました</span></div>
  </div>
  <div class="abs info-scroll"></div>
</section>

<section class="abs contact">
  <div class="abs bg-word">CONTACT</div>
  <h2 class="abs contact-title">お問い合わせ</h2>
  <div class="abs contact-box" style="left:260px">
    <h3>お電話でのお問い合わせ</h3>
    <div class="contact-tel">
      <svg width="20" height="20" viewBox="0 0 24 24"><path fill="#00008B" d="M6.6 10.8a15.1 15.1 0 006.6 6.6l2.2-2.2c.3-.3.7-.4 1-.2 1.1.4 2.3.6 3.6.6.6 0 1 .4 1 1V20c0 .6-.4 1-1 1A17 17 0 013 4c0-.6.4-1 1-1h3.5c.6 0 1 .4 1 1 0 1.3.2 2.5.6 3.6.1.3 0 .7-.2 1z"/></svg>
      000-000-0000
    </div>
    <p class="contact-hours">受付時間 9:00〜18:00（土日祝除く）</p>
  </div>
  <div class="abs contact-box" style="left:608px">
    <h3>メールでのお問い合わせ</h3>
    <div class="contact-mail">
      <svg width="14" height="10" viewBox="0 0 14 10"><rect x=".5" y=".5" width="13" height="9" fill="none" stroke="#fff"/><path d="M.5.5l6.5 5 6.5-5" fill="none" stroke="#fff"/></svg>
      メールフォームはこちら
    </div>
  </div>
</section>

<footer>
  <div class="abs footer-company">
    <h2>株式会社〇〇〇〇</h2>
    <p>〒000-0000<br>東京都〇〇区〇〇町0-0-0</p>
    <p class="tel">TEL：0000-000-0000<br>FAX：0000-000-0000</p>
  </div>
  <nav class="abs footer-nav">
    <a href="#">ホーム</a><a href="#">〇〇〇〇について</a><a href="#">業務案内</a><a href="#">お知らせ</a>
  </nav>
  <div class="abs footer-sub">
    <span><svg width="10" height="14" viewBox="0 0 10 14"><path fill="#00008B" d="M5 0a5 5 0 015 5c0 3.5-5 9-5 9S0 8.5 0 5a5 5 0 015-5zm0 3a2 2 0 100 4 2 2 0 000-4z"/></svg>MAP</span>
    <span>採用情報</span>
  </div>
  <div class="abs copyright">© 株式会社〇〇〇〇 All Rights Reserved.</div>
</footer>

</body>
</html>
```